Landcape Construction Company needs a flyer to catch attention

A flyer that can be displayed at several different stores detailing our skills, work produced, experience and contact details. Information can be extracted from our website www.brvkw.co.nz. The flyer should feel very green, with addition of pics of work completed as well as stock images of lush green plants, lawns, landscape or similar. Needs to be eye catching with just enough information to express our experience and commitment to high standards

Target Market(s)

Residential
Landscape Architects

Industry/Entity Type

Landscaping

Font styles to use
Serif

Colors
abd037

Requirements
Must have
• Our logo
Experience
Services offered including pictures
All information avail on our website www.brvkw.co.nz
Nice to have
• stock images of lush greenery like a garden after fresh rainfall
Should not have
• Nothing comes to mind

```html
<!DOCTYPE html>
<html lang="en">
<head>
<meta charset="utf-8">
<title>The Fernbrook Landscaping Company – Flyer</title>
<link href="https://fonts.googleapis.com/css2?family=Cinzel:wght@500;700&family=Montserrat:wght@400;500;700&display=swap" rel="stylesheet">
<style>
:root{
  --bg:#e7fbc8;
  --shadow:#d5e8bb;
  --green-dark:#0e7a27;
  --green-mid:#1c8b2e;
  --green-light:#8cc63f;
  --green-brand:#abd037;
  --text:#3d3d3d;
  --muted:#6d6d6d;
  --card:#e6e6e6;
  --white:#ffffff;
}
*{margin:0;padding:0;box-sizing:border-box}
html,body{width:1200px;height:1200px;overflow:hidden;background:var(--bg)}
body{position:relative;font-family:'Montserrat',sans-serif;color:var(--text)}
.backing{position:absolute;width:440px;height:932px;background:var(--shadow);top:155px}
.backing--front{left:94px}
.backing--back{left:619px}
.page{position:absolute;top:116px;width:440px;height:932px;background:var(--white);overflow:hidden}
.page--front{left:137px}
.page--back{left:663px}
.layer{position:absolute;left:0;top:0;width:440px;height:932px}
.photo{position:absolute}
.round{border-radius:50%;border:6px solid var(--green-light);background-clip:padding-box}

/* front */
.hero-photo{left:0;top:0;width:440px;height:450px;background:linear-gradient(180deg,#c9ccce 0%,#9aa58f 18%,#4f8a2e 38%,#4e9b2a 55%,#6fb83a 100%)}
.hedge-photo{left:195px;top:218px;width:168px;height:168px;background:radial-gradient(circle at 40% 50%,#6f8a55,#3e5a2c 70%,#9aa3a0)}
.badge{position:absolute;left:79px;top:299px;width:128px;height:128px;border-radius:50%;background:radial-gradient(circle at 50% 35%,#c9ea7a,#8cc63f 70%);border:4px solid var(--green-light);box-shadow:inset 0 0 0 2px var(--green-dark);text-align:center;color:#222}
.badge__num{font-family:'Montserrat',sans-serif;font-weight:700;font-size:52px;line-height:1;margin-top:14px;letter-spacing:-2px}
.badge__label{font-weight:700;font-size:11.5px;line-height:14px;margin-top:2px}
.brand{position:absolute;left:16px;top:14px;width:138px;text-align:center}
.brand__mark{width:70px;height:70px;border-radius:50%;background:var(--green-mid);margin:0 auto 9px}
.brand__name{font-family:'Montserrat',sans-serif;font-weight:700;font-size:10px;line-height:12px;color:var(--green-dark);white-space:nowrap}
.title{position:absolute;left:0;top:456px;width:440px;text-align:center;font-family:'Cinzel',serif;font-weight:700}
.title__top{font-size:30px;color:var(--green-dark);line-height:34px}
.title__bottom{font-size:26px;color:var(--green-light);line-height:34px;margin-top:2px}
.divider{position:absolute;left:40px;top:537px;width:370px;height:10px}
.intro{position:absolute;left:39px;top:558px;width:362px;font-size:10.4px;line-height:13.2px;text-align:justify;text-align-last:center;color:var(--text)}
.intro p+p{margin-top:13px}
.ground-photo{left:0;top:690px;width:440px;height:242px;background:linear-gradient(180deg,#ffffff 0%,#cfe2b0 22%,#4f8d34 42%,#9fcf3c 65%,#c3df3e 100%)}
.contacts{position:absolute;left:52px;top:848px;list-style:none}
.contacts li{display:flex;align-items:center;height:23px;font-weight:700;font-size:13.5px;color:var(--white)}
.contacts svg{width:13px;height:13px;margin-right:9px;flex:none}

/* back */
.section-title{position:absolute;left:0;width:440px;text-align:center;font-family:'Cinzel',serif;font-weight:500}
.about__title{top:33px;font-size:17px;color:var(--green-brand)}
.about__lead{position:absolute;left:35px;top:68px;width:364px;font-weight:700;font-size:10.2px;line-height:13.1px;color:var(--white);text-align:justify;text-align-last:center}
.about__body{position:absolute;left:35px;top:148px;width:364px;font-size:8.7px;line-height:11.3px;color:var(--white);text-align:justify;text-align-last:center}
.work-a{left:11px;top:310px;width:136px;height:136px;background:linear-gradient(180deg,#7fae5a 0%,#5aa93a 45%,#6bbd35 75%,#cfd2c8 100%)}
.work-b{left:151px;top:281px;width:138px;height:138px;background:linear-gradient(180deg,#c7d6e2 0%,#e9eef2 35%,#4d6b45 52%,#b9bfc4 65%,#9ea5aa 100%)}
.work-c{left:288px;top:236px;width:138px;height:138px;background:linear-gradient(135deg,#e3b78a,#c88e5c 55%,#f0d9bf)}
.services__title{top:448px;font-size:21px;color:var(--green-dark);font-weight:700}
.services__intro{position:absolute;left:35px;top:480px;width:370px;font-size:8.9px;line-height:11.4px;color:var(--muted);text-align:justify;text-align-last:center}
.service-card{position:absolute;top:544px;width:133px;height:235px;background:var(--card);border-radius:10px}
.service-card--1{left:15px}.service-card--2{left:153px}.service-card--3{left:289px}
.service-card__photo{position:absolute;left:8px;top:7px;width:117px;height:93px;border-radius:10px;border:3px solid var(--white);box-shadow:0 2px 4px rgba(0,0,0,.25)}
.photo-timber{background:linear-gradient(180deg,#d7ecb8 0%,#b6d98a 45%,#b7865a 55%,#8a5a32 100%)}
.photo-paving{background:linear-gradient(135deg,#8e9091,#6f7172 60%,#9b9d9e)}
.photo-lawn{background:linear-gradient(160deg,#e1ddd4 0%,#d3cfc6 25%,#5ea32f 45%,#7dbd3c 100%)}
.service-card ul{position:absolute;left:0;top:114px;width:133px;list-style:none;text-align:center}
.service-card li{font-size:9.4px;height:22px;line-height:22px;color:#333;margin:0 auto;width:76px;white-space:nowrap;display:flex;justify-content:center;border-bottom:1px solid #cfcfcf}
.service-card li:last-child{border-bottom:none}
.fade-photo{left:0;top:790px;width:440px;height:142px;background:linear-gradient(180deg,#ffffff 0%,#dcdcdc 40%,#f2f2f2 100%)}
</style>
</head>
<body>
<div class="backing backing--front"></div>
<div class="backing backing--back"></div>

<section class="page page--front">
  <div class="photo hero-photo" role="img" aria-label="Photo of a formal garden with striped lawn, clipped hedges and large trees"></div>
  <div class="photo ground-photo" role="img" aria-label="Photo of a sunny open lawn bordered by lush trees"></div>
  <svg class="layer" viewBox="0 0 440 932" aria-hidden="true">
    <path d="M0 0H232C228 95 150 152 0 160Z" fill="#ffffff"/>
    <path d="M232 0H245C242 105 160 170 0 176V160C150 152 228 95 232 0Z" fill="#0e7a27"/>
    <path d="M222 0H232C228 95 150 152 0 160V154C140 146 218 90 222 0Z" fill="#8cc63f"/>
    <path d="M0 360C60 362 110 378 150 402C100 416 50 418 0 412Z" fill="#0e7a27"/>
    <path d="M0 412C60 420 120 412 170 396C250 372 320 350 372 372C405 388 428 415 440 440V700H0Z" fill="#ffffff"/>
    <path d="M300 300C365 300 415 345 440 400V432C420 380 370 330 300 318Z" fill="#8cc63f"/>
    <path d="M0 828C80 778 190 776 262 806C342 842 400 875 440 886V932H0Z" fill="#5aaa2e"/>
    <path d="M0 846C90 796 200 796 270 826C350 860 410 886 440 896V932H0Z" fill="#0e7a27"/>
  </svg>
  <div class="photo hedge-photo round" role="img" aria-label="Close-up photo of a rounded flowering hedge beside paving"></div>
  <div class="badge"><div class="badge__num">25</div><div class="badge__label">YEARS<br>EXPERIENCE</div></div>
  <div class="brand"><div class="brand__mark"></div><div class="brand__name">The Fernbrook<br>Landscaping Company</div></div>
  <h1 class="title"><div class="title__top">The Fernbrook</div><div class="title__bottom">LANDSCAPING COMPANY</div></h1>
  <svg class="divider" viewBox="0 0 370 10" aria-hidden="true">
    <line x1="0" y1="5" x2="153" y2="5" stroke="#0e7a27" stroke-width="1.5"/>
    <line x1="217" y1="5" x2="370" y2="5" stroke="#0e7a27" stroke-width="1.5"/>
    <path d="M165 0l5 5-5 5-5-5zM185 0l5 5-5 5-5-5zM205 0l5 5-5 5-5-5z" fill="#8cc63f"/>
  </svg>
  <div class="intro">
    <p>With more than 25 years experience in the landscaping industry, The Fernbrook Landscaping Company offers services to large or small residential and commercial projects. Based in Canterbury, we are locally owned and operated.</p>
    <p>Whether you have a blank canvas or are looking to rejuvenate your property we are able to advise and make the process easy and stress free. From paving, pergolas and decks to concrete or planting your dream garden we have the expertise to help.</p>
  </div>
  <ul class="contacts">
    <li><svg viewBox="0 0 16 16"><path d="M3 1l3 3-1.5 2c1 2 3 4 5 5L11.5 9.5l3 3-2 2.5C7 14 2 9 1 3.5Z" fill="#8cc63f"/></svg>021 555 0142</li>
    <li><svg viewBox="0 0 16 16"><rect x="1" y="3" width="14" height="10" fill="#8cc63f"/><path d="M1 3l7 6 7-6" stroke="#0e7a27" fill="none" stroke-width="1.3"/></svg>mark@brvkw.co.nz</li>
    <li><svg viewBox="0 0 16 16"><circle cx="8" cy="8" r="7" fill="#8cc63f"/><path d="M1 8h14M8 1c-3 4-3 10 0 14M8 1c3 4 3 10 0 14" stroke="#0e7a27" fill="none"/></svg>www.brvkw.co.nz</li>
  </ul>
</section>

<section class="page page--back">
  <div class="photo fade-photo" role="img" aria-label="Faded photo of a park with trees"></div>
  <svg class="layer" viewBox="0 0 440 932" aria-hidden="true">
    <path d="M0 0H440V330C380 300 300 330 220 352C140 372 60 366 0 355Z" fill="#0e7a27"/>
    <path d="M0 355C60 366 140 372 220 352C300 330 380 300 440 330V338C380 310 300 340 220 360C140 380 60 374 0 362Z" fill="#8cc63f"/>
    <path d="M0 860C40 800 130 790 200 810C300 840 380 898 440 905V932H0Z" fill="#5aaa2e"/>
    <path d="M0 876C50 816 140 806 210 826C310 856 380 906 440 912V932H0Z" fill="#0e7a27"/>
  </svg>
  <h2 class="section-title about__title">ABOUT US</h2>
  <p class="about__lead">Our company is built on honesty, teamwork, sound knowledge and a determination to provide our customers with the highest quality product and service. We are a small team of highly skilled, dedicated and reliable professionals who complete projects efficiently and with outstanding workmanship.</p>
  <p class="about__body">We hold Stonelay Pro Accreditation status making us preferred installers of this paving system. To achieve this we had to show we had a solid understanding of the system and the skill set to ensure workmanship was held to the highest standard. How we work is simple. We will listen, get a clear idea of your vision and offer practical advice in order to achieve the best outcome within your budget and scope. An initial consultation is free so give us a call and let's chat about getting the best solution to your landscaping needs.</p>
  <div class="photo work-a round" role="img" aria-label="Photo of a curved lawn edged with a garden border"></div>
  <div class="photo work-b round" role="img" aria-label="Photo of a large paved plaza with trees beyond"></div>
  <div class="photo work-c round" role="img" aria-label="Photo of a timber deck and pergola walkway"></div>
  <h2 class="section-title services__title">OUR SERVICES</h2>
  <p class="services__intro">As a full construction landscaping company, we formally offer the following services. However, we regularly work with clients who want something a little out of the box. If there is something in particular you are after, we are happy to discuss options with you.</p>
  <div class="service-card service-card--1">
    <div class="service-card__photo photo-timber" role="img" aria-label="Photo of a timber tabletop against green foliage"></div>
    <ul><li>PATIOS</li><li>PAVING</li><li>CONCRETE</li><li>WATER FEATURES</li><li>DECKING</li></ul>
  </div>
  <div class="service-card service-card--2">
    <div class="service-card__photo photo-paving" role="img" aria-label="Photo of grey concrete paving slabs"></div>
    <ul><li>FENCING</li><li>BOARDWALKS</li><li>TIMBER</li><li>PLANTER BOXES</li><li>PERGOLAS</li></ul>
  </div>
  <div class="service-card service-card--3">
    <div class="service-card__photo photo-lawn" role="img" aria-label="Photo of a lawn with a sprinkler watering beside gravel"></div>
    <ul><li>RETAINING WALLS</li><li>GARDENS &amp; LAWNS</li><li>IRRIGATION</li><li>PROJECT MANAGEMENT</li><li>CONSULTATION</li></ul>
  </div>
  <ul class="contacts">
    <li><svg viewBox="0 0 16 16"><path d="M3 1l3 3-1.5 2c1 2 3 4 5 5L11.5 9.5l3 3-2 2.5C7 14 2 9 1 3.5Z" fill="#8cc63f"/></svg>021 555 0142</li>
    <li><svg viewBox="0 0 16 16"><rect x="1" y="3" width="14" height="10" fill="#8cc63f"/><path d="M1 3l7 6 7-6" stroke="#0e7a27" fill="none" stroke-width="1.3"/></svg>mark@brvkw.co.nz</li>
    <li><svg viewBox="0 0 16 16"><circle cx="8" cy="8" r="7" fill="#8cc63f"/><path d="M1 8h14M8 1c-3 4-3 10 0 14M8 1c3 4 3 10 0 14" stroke="#0e7a27" fill="none"/></svg>www.brvkw.co.nz</li>
  </ul>
</section>
</body>
</html>
```